Car wrap for landscaping/gardening company (in Portuguese)

This is a landscaping company that is fully electric, providing, silent, emissions-free landscaping to the community. I am requesting a wrap for the residential van that will be used for this service.

The key things that the wrap must convey, besides the logo of the company, is:
(1) 100% electric (100% Elétrico)
(2) Silent (Silencioso)
(3) No emissions (Sem Emissões)
I envision three large, round icons with a simple image illustrating each of these concepts, and below each icon the text in Portuguese. The van only has to have the logo and the icons, plus a space for phone number and website which can be a little smaller. Use bold colors, make it modern. Don't make it flowery, that will not distinguish the van.

An additional icon can also be added for Customer Service. So possibly 4 icons, with the 4th one saying "Serviço ao Cliente." I am interested in seeing alternatives with 3 and 4 icons.

Please check out the sample that I sent. I like this wrap because it is simple and very visible. It has a lot of text in the rear though which is difficult to read. I don't want this kind of text. Just the icons and the titles. Make it super clear.

The service is high tech, innovative, and premium. It is not a normal landscaping company. I want to attract high end customers who demand the best, who want landscaping that is silent and clean for the environment.

Target Market(s)

Residential customers with patios, large houses, looking for high tech landscaping service and willing to pay a premium

Industry/Entity Type

Landscaping, Gardening

Font styles to use
Sans Serif

Requirements
Must have
• Please use the logo that I have provided. I also need three icons, well displayed, each one representing an aspect of our service: (1) 100% ELÉTRICO (2) SILENCIOSO (3) SEM EMISSÕES. In Portuguese it means 100% electric, Silent, No emissions. Can be three round icons below the logo, very prominent so that people know what the service is about. Also need a place to put two phone numbers, on the back and on the door, as well as the website.
Nice to have
• The picture that I showed is a good example of a blue car wrap. This can work but has to be in green or brown (landscaping colors). I like it because it is bold and visible, and doesn't have too many decorative features. It is very modern and simple, which is consistent with the theme that I am looking for.
Should not have
• Flowery shapes, too much decoration, curvy lines, excessive text

```html
<!DOCTYPE html>
<html lang="pt">
<head>
<meta charset="UTF-8">
<title>Quintas Calmas – Van Wrap</title>
<link href="https://fonts.googleapis.com/css2?family=Poppins:wght@500;600&family=Oswald:wght@600&display=swap" rel="stylesheet">
<style>
  :root {
    --green: #1a8a2e;
    --green-deep: #167a28;
    --brown: #8a5a2e;
    --white: #ffffff;
    --canvas: #ffffff;
  }
  * { margin: 0; padding: 0; box-sizing: border-box; }
  html, body { width: 1200px; height: 1200px; overflow: hidden; background: var(--canvas); }
  .wrap-side { position: relative; width: 1200px; height: 1200px; }
  .bands { position: absolute; inset: 0; }
  .brand-name {
    position: absolute; left: 640px; top: 382px; width: 440px;
    font-family: "Poppins", sans-serif; font-weight: 500;
    color: var(--green); font-size: 82px; line-height: 84px;
    letter-spacing: 3px; text-align: center; text-transform: uppercase;
  }
  .band-watermark {
    position: absolute; left: 670px; top: 628px; width: 440px;
    font-family: "Poppins", sans-serif; font-weight: 500;
    color: var(--green-deep); font-size: 70px; line-height: 76px;
    letter-spacing: 3px; text-align: center; opacity: .55;
  }
  .phone {
    position: absolute; left: 729px; top: 580px;
    font-family: "Poppins", sans-serif; font-weight: 600;
    color: var(--white); font-size: 36px; letter-spacing: 2px;
  }
  .website {
    position: absolute; left: 135px; top: 601px;
    font-family: "Poppins", sans-serif; font-weight: 600;
    color: var(--brown); font-size: 15px;
  }
  .features { position: absolute; left: 410px; top: 566px; list-style: none; }
  .feature { display: flex; align-items: center; height: 30px; margin-bottom: 1px; }
  .feature svg { width: 27px; height: 27px; margin-right: 9px; flex: none; }
  .feature span {
    font-family: "Oswald", sans-serif; font-weight: 600;
    color: var(--green); font-size: 16px; letter-spacing: .3px;
  }
</style>
</head>
<body>
<main class="wrap-side">
  <svg class="bands" width="1200" height="1200" viewBox="0 0 1200 1200">
    <polygon class="band-green" fill="#1a8a2e" points="675,625 1119,625 1119,781 531,781"/>
    <polygon class="band-brown" fill="#8a5a2e" points="494,781 700,578 1119,578 1119,625 675,625 531,781"/>
  </svg>

  <div class="band-watermark" aria-hidden="true">QUINTAS<br>CALMAS</div>

  <h1 class="brand-name">Quintas<br>Calmas</h1>

  <div class="phone">555-014-2290</div>
  <div class="website">www.quintascalmas.com</div>

  <ul class="features">
    <li class="feature">
      <svg viewBox="0 0 28 28"><circle cx="14" cy="14" r="13" fill="#8a5a2e"/><circle cx="14" cy="14" r="9.5" fill="none" stroke="#fff" stroke-width="1.6"/><polygon points="15.5,7 10,15 13.5,15 12.5,21 18,13 14.5,13" fill="#fff"/></svg>
      <span>100% ELÉTRICO</span>
    </li>
    <li class="feature">
      <svg viewBox="0 0 28 28"><circle cx="14" cy="14" r="13" fill="#8a5a2e"/><polygon points="7,11.5 10,11.5 14,8 14,20 10,16.5 7,16.5" fill="#fff"/><path d="M16.5 11.5 L21 16.5 M21 11.5 L16.5 16.5" stroke="#fff" stroke-width="1.6" stroke-linecap="round"/></svg>
      <span>SILENCIOSO</span>
    </li>
    <li class="feature">
      <svg viewBox="0 0 28 28"><circle cx="14" cy="14" r="13" fill="#8a5a2e"/><path d="M9 18 h10 a3 3 0 0 0 0-6 a4.5 4.5 0 0 0-8.5-1 a3.5 3.5 0 0 0-1.5 7z" fill="#fff"/><circle cx="14" cy="14" r="9.5" fill="none" stroke="#fff" stroke-width="1.6"/><line x1="7.5" y1="20.5" x2="20.5" y2="7.5" stroke="#8a5a2e" stroke-width="3"/><line x1="7.5" y1="20.5" x2="20.5" y2="7.5" stroke="#fff" stroke-width="1.6"/></svg>
      <span>SEM EMISSÕES</span>
    </li>
    <li class="feature">
      <svg viewBox="0 0 28 28"><circle cx="14" cy="14" r="13" fill="#8a5a2e"/><path d="M8 15 v-2 a6 6 0 0 1 12 0 v2" fill="none" stroke="#fff" stroke-width="1.8"/><rect x="6.5" y="13.5" width="3.5" height="5.5" rx="1.2" fill="#fff"/><rect x="18" y="13.5" width="3.5" height="5.5" rx="1.2" fill="#fff"/><path d="M20 19 q0 2.5 -4 2.5" fill="none" stroke="#fff" stroke-width="1.4"/></svg>
      <span>SERVIÇO AO CLIENTE</span>
    </li>
  </ul>
</main>
</body>
</html>
```